Crestfield Automotive Business Card

Automotive repair , all makes including Asian and European Imports. QMR Certified (Logo),Chatterbook (logo), Pingly+ (logo)

Industry/Entity Type

Automotive

Contact Information for Business Card

Crestfield Automotive, Ray Hobart Owner, 3817 Larch Ave. Worthington, Mn 58402. Website crestfieldautomotive.example. (555) 641-0938

```html
<!DOCTYPE html>
<html lang="en">
<head>
<meta charset="utf-8">
<title>Crestfield Automotive – Business Card</title>
<link rel="stylesheet" href="https://fonts.googleapis.com/css2?family=Jura:wght@500;700&display=swap">
<style>
  :root {
    --backdrop: #d8d3cb;
    --card: #f3f1ee;
    --card-edge: #e4e1dc;
    --ink: #3a3a3c;
    --navy: #1f3a94;
    --brand-blue: #123a9c;
    --brand-red: #d3232f;
    --rule: #9b9a98;
    --white: #ffffff;
  }
  * { box-sizing: border-box; margin: 0; padding: 0; }
  html, body { width: 1200px; height: 768px; overflow: hidden; }
  body {
    background: var(--backdrop);
    font-family: "Jura", sans-serif;
    color: var(--ink);
    position: relative;
  }
  .card {
    position: absolute;
    left: 100px; top: 94px;
    width: 1000px; height: 581px;
    border-radius: 30px;
    background: linear-gradient(160deg, #f7f6f4 0%, var(--card) 55%, #ebe8e4 100%);
    border: 2px solid var(--card-edge);
    overflow: hidden;
    box-shadow: 0 10px 30px rgba(0,0,0,.12);
  }
  .brand {
    position: absolute;
    left: 600px; top: 74px;
    width: 310px;
    text-align: center;
    font-weight: 700;
    font-size: 44px;
    line-height: 1.05;
    color: var(--brand-blue);
    letter-spacing: .5px;
  }
  .person-name {
    position: absolute; left: 38px; top: 190px;
    font-size: 29px; font-weight: 700; letter-spacing: 1.5px;
  }
  .person-role {
    position: absolute; left: 38px; top: 242px;
    font-size: 23px; font-weight: 700; color: var(--navy);
  }
  .divider {
    position: absolute; left: 58px; top: 288px;
    width: 880px; height: 3px;
    background: linear-gradient(90deg, rgba(155,154,152,.2), var(--rule) 35%, var(--rule) 75%, rgba(155,154,152,.1));
  }
  .address {
    position: absolute; left: 38px; top: 382px;
    font-size: 23px; font-weight: 700; line-height: 32px;
  }
  .contacts {
    position: absolute; right: 32px; top: 310px;
    list-style: none;
    text-align: right;
  }
  .contacts li {
    display: flex; justify-content: flex-end; align-items: center;
    gap: 14px; font-weight: 700;
  }
  .contacts .big { font-size: 21px; height: 48px; }
  .contacts .small { font-size: 19px; height: 34px; }
  .contacts svg { width: 22px; height: 22px; fill: var(--navy); flex: none; }
  .band {
    position: absolute; left: 0; bottom: 0;
    width: 1000px; height: 61px;
  }
  .band-web {
    position: absolute; left: 38px; bottom: 18px;
    color: var(--white); font-size: 19px; font-weight: 700;
  }
</style>
</head>
<body>
  <main class="card">
    <div class="brand">Crestfield<br>Automotive</div>

    <h1 class="person-name">RAY HOBART</h1>
    <p class="person-role">Owner</p>
    <div class="divider"></div>

    <address class="address" style="font-style:normal">3817 Larch Ave.<br>Worthington, MN 58402</address>

    <ul class="contacts">
      <li class="big">(555) 641-0938
        <svg viewBox="0 0 24 24" aria-hidden="true"><path d="M6.6 10.8a15 15 0 0 0 6.6 6.6l2.2-2.2c.3-.3.7-.4 1-.2 1.1.4 2.3.6 3.6.6.6 0 1 .4 1 1V20c0 .6-.4 1-1 1A17 17 0 0 1 3 4c0-.6.4-1 1-1h3.5c.6 0 1 .4 1 1 0 1.3.2 2.5.6 3.6.1.3 0 .7-.2 1z"/></svg>
      </li>
      <li class="big">(555) 641-0938
        <svg viewBox="0 0 24 24" aria-hidden="true"><path d="M7 1h10a2 2 0 0 1 2 2v18a2 2 0 0 1-2 2H7a2 2 0 0 1-2-2V3a2 2 0 0 1 2-2zm0 3v14h10V4zm5 15.2a1.2 1.2 0 1 0 0 2.4 1.2 1.2 0 0 0 0-2.4z"/></svg>
      </li>
      <li class="big">(555) 641-0938
        <svg viewBox="0 0 24 24" aria-hidden="true"><path d="M8 2h8v5H8zM4 8h16a2 2 0 0 1 2 2v11H2V10a2 2 0 0 1 2-2zm3 4v2h2v-2zm4 0v2h2v-2zm4 0v2h2v-2zm-8 4v2h2v-2zm4 0v2h2v-2zm4 0v2h2v-2z"/></svg>
      </li>
      <li class="small">service@crestfield.example
        <svg viewBox="0 0 24 24" aria-hidden="true"><path d="M2 5h20v14H2zm2 2v.5l8 5 8-5V7zm0 2.8V17h16V9.8l-8 5z"/></svg>
      </li>
      <li class="small">crestfieldautomotive.example
        <svg viewBox="0 0 24 24" aria-hidden="true"><path d="M12 2a10 10 0 1 0 0 20 10 10 0 0 0 0-20zm6.9 6h-3a15 15 0 0 0-1.3-3.9A8 8 0 0 1 18.9 8zM12 4c.8 1.1 1.5 2.5 1.9 4h-3.8c.4-1.5 1.1-2.9 1.9-4zM4.3 14a8 8 0 0 1 0-4h3.3a16 16 0 0 0 0 4zm.8 2h3a15 15 0 0 0 1.3 3.9A8 8 0 0 1 5.1 16zm3-8h-3a8 8 0 0 1 4.3-3.9A15 15 0 0 0 8.1 8zM12 20c-.8-1.1-1.5-2.5-1.9-4h3.8c-.4 1.5-1.1 2.9-1.9 4zm2.3-6H9.7a14 14 0 0 1 0-4h4.6a14 14 0 0 1 0 4zm.3 5.9a15 15 0 0 0 1.3-3.9h3a8 8 0 0 1-4.3 3.9zm1.8-5.9a16 16 0 0 0 0-4h3.3a8 8 0 0 1 0 4z"/></svg>
      </li>
    </ul>

    <svg class="band" viewBox="0 0 1000 61" preserveAspectRatio="none" aria-hidden="true">
      <path d="M0 2 H385 C402 2 410 8 416 20 L436 61 H0 Z" fill="var(--brand-blue)"/>
      <path d="M424 20 H1000 V61 H446 L432 30 C430 25 428 22 424 20 Z" fill="var(--brand-red)"/>
    </svg>
    <p class="band-web">crestfieldautomotive.example</p>
  </main>
</body>
</html>
```